Building company with a modern and unique product looking for a business card to help us stand out

We currently have a logo but as our business has grown, we feel that our business card is not reflecting our modern and high quality product and help us stand out from the crowd. Our business is mainly in the construction of new homes using a unique method and materials that makes our homes fire proof, vermin and pest resistant and rated to the maximum cyclone category (category 5). We need a business card that helps us stand out as well as communicating professionalism, high quality and trustworthiness. I have attached our current logo with a black and white option, as well as our business card which is double sided. We would like to retain as much of the information that is currently on our business cards, but presented in a more sleek way. We do like our current colour palette ( white, black, yellow and grey) and have been looking primarily at business cards with a black background however we are open to other combinations of colour and layout as long as we stand out. Please feel free to tweak our logo to make it more suitable for a business card, we like the black option that we use but we have had trouble trying to get the white area to match the rest of the logo and blend effectively into a business card. Please do not hesitate to contact us with any questions as we really want this to be successful!

Target Market(s)

Large contracts including government and larger companies

Industry/Entity Type

Business

We will be providing this business card to potential clients including key government ministers and large funding companies, our business card should show that we are professional and reliable.

Requirements
Must have
• It must be easy to read and pleasing to the eye, It must contain as much of the information on the current business card and unless something really stands out, we will most likely pick a design that has all of the information included. It must include our logo of course and have some colour included.
Nice to have
• We are looking for a high end business card and would like to see designs that reflect this. We like the gloss/matte contrast, plastic cards with opaque/coloured areas and unique features not seen on everyday paper business cards. It would be nice to see a few different colour combinations, we are open to new ideas so please feel free to take some artistic licence.
Should not have
• Must not be too busy, difficult to read or be distracting from the information conveyed. Other than this please feel free to add your own touches and make it unique!

```html
<!DOCTYPE html>
<html lang="en">
<head>
<meta charset="utf-8">
<title>Norvale Building Company – Business Card</title>
<link href="https://fonts.googleapis.com/css2?family=Open+Sans:wght@400;600;700&display=swap" rel="stylesheet">
<style>
  :root{
    --bg:#ecebe8;
    --card-black:#0d0d0d;
    --card-black-soft:#1c1c1c;
    --gold-deep:#c39a1f;
    --gold-light:#e6c95a;
    --ink:#111111;
    --white:#ffffff;
    --grey:#b9b9b9;
  }
  html,body{margin:0;padding:0;overflow:hidden;}
  body{
    width:1200px;height:913px;background:var(--bg);
    font-family:"Open Sans",Arial,sans-serif;
    position:relative;
  }
  .card{
    position:absolute;width:500px;height:290px;
    border-radius:22px;overflow:hidden;
    box-shadow:0 10px 30px rgba(0,0,0,.25);
  }
  .card svg{display:block;}
  .card--front{left:85px;top:150px;}
  .card--back{left:615px;top:470px;}
  .brand-name{font-family:"Open Sans",Arial,sans-serif;font-weight:600;fill:var(--white);}
  .person-name{font-weight:700;font-size:22px;fill:var(--ink);}
  .person-role{font-weight:400;font-size:13px;fill:var(--white);}
  .contact{font-weight:400;font-size:13.5px;fill:var(--ink);}
  .contact--abn{font-weight:600;}
  .tagline{font-weight:400;font-size:14px;fill:var(--white);}
</style>
</head>
<body>

<div class="card card--front">
  <svg width="500" height="290" viewBox="0 0 500 290">
    <defs>
      <linearGradient id="goldFill" x1="0" y1="0" x2="1" y2="1">
        <stop offset="0" stop-color="var(--gold-light)"/>
        <stop offset="1" stop-color="var(--gold-deep)"/>
      </linearGradient>
      <linearGradient id="blackFill" x1="0" y1="0" x2="1" y2="1">
        <stop offset="0" stop-color="var(--card-black-soft)"/>
        <stop offset="1" stop-color="var(--card-black)"/>
      </linearGradient>
    </defs>
    <rect class="front-base" width="500" height="290" fill="url(#blackFill)"/>
    <circle class="front-arc-line" cx="-40" cy="290" r="388" fill="none" stroke="var(--white)" stroke-width="3"/>
    <circle class="front-gold-panel" cx="-40" cy="290" r="380" fill="url(#goldFill)"/>

    <g class="front-brand">
      <rect x="318" y="96" width="14" height="14" fill="var(--gold-light)"/>
      <text class="brand-name" x="340" y="110" font-size="20">Norvale</text>
      <text class="brand-name" x="340" y="134" font-size="14">Building Company</text>
    </g>

    <g class="front-details">
      <text class="person-name" x="36" y="150">Calvin Moreton</text>
      <text class="person-role" x="36" y="170">Managing Director</text>
      <text class="contact contact--abn" x="36" y="192">ABN: 48 213 650 971</text>

      <g class="icon-phone" transform="translate(36,207)">
        <path d="M2 1 L5 0 L7 4 L5 5.5 Q6.5 8.5 9 10 L10.5 8 L14 10 L13 13 Q6 13 2 6 Z" fill="var(--white)"/>
      </g>
      <text class="contact" x="58" y="219">0400 555 182</text>

      <g class="icon-landline" transform="translate(36,228)">
        <rect x="0" y="4" width="14" height="9" rx="2" fill="var(--white)"/>
        <path d="M0 5 Q7 -2 14 5" fill="none" stroke="var(--white)" stroke-width="2"/>
      </g>
      <text class="contact" x="58" y="240">(02) 5550 1234</text>

      <g class="icon-mail" transform="translate(36,250)">
        <rect x="0" y="0" width="14" height="10" fill="none" stroke="var(--white)" stroke-width="1.6"/>
        <path d="M0 0 L7 6 L14 0" fill="none" stroke="var(--white)" stroke-width="1.6"/>
      </g>
      <text class="contact" x="58" y="261">hello@norvalebuilding.com</text>
    </g>
  </svg>
</div>

<div class="card card--back">
  <svg width="500" height="290" viewBox="0 0 500 290">
    <defs>
      <linearGradient id="blackFillBack" x1="0" y1="0" x2="1" y2="1">
        <stop offset="0" stop-color="var(--card-black-soft)"/>
        <stop offset="1" stop-color="var(--card-black)"/>
      </linearGradient>
    </defs>
    <rect class="back-base" width="500" height="290" fill="url(#blackFillBack)"/>

    <g class="back-brand">
      <rect x="150" y="64" width="16" height="16" fill="var(--gold-light)"/>
      <text class="brand-name" x="176" y="80" font-size="26">Norvale</text>
      <text class="brand-name" x="176" y="108" font-size="17">Building Company</text>
    </g>

    <g class="back-tagline" text-anchor="middle">
      <text class="tagline" x="250" y="160">Specialising in</text>
      <text class="tagline" x="250" y="179">Homes that are</text>
      <text class="tagline" x="250" y="198">Fire Proof</text>
      <text class="tagline" x="250" y="217">Climate Proof</text>
      <text class="tagline" x="250" y="236">Cyclone Rated (Cat. 5)</text>
    </g>
  </svg>
</div>

</body>
</html>
```